Homepage for a Workout + Food Tracking Mobile App

We need a design for the homepage of our workout and food tracking app called FitBrook (working name, most likely not finalized). The app has many uses, namely a "Strength Review", food logging, workout tracking, statistics/analytics, an AI powered form review tool and an ability to ask an AI any workout, nutrition or app related questions. The homepage should feature some way to access the above listed features as well as an outline, 3d design, diagram or any other way to represent the human body split up into muscle groups for the user to see what muscles they've hit in any amount of time. There should be a section for a profile picture, username, "trophy case" with room for ideally 3 small "trophy" icons.
The main colour should be gold/dark yellow (I used #DEA30A) but I am very flexible on that and I'm curious to try out other colours. The background colour I am also flexible on, I went with a dark gray.
The screenshot I uploaded is in no way what your design needs to look like. Use it more to check what buttons and elements should be present.
I'll likely need more designs for other screens in the future and will be happy to work further with the designer chosen.
Target Market(s)
Gymgoers, People on a diet, Weightlifters,
Look and feel

```html
<!DOCTYPE html>
<html lang="en">
<head>
<meta charset="utf-8">
<title>FitBrook – Home</title>
<link href="https://fonts.googleapis.com/css2?family=Inter:wght@400;500;600;700;800&display=swap" rel="stylesheet">
<style>
  :root{
    --canvas:#fdf0e0;
    --screen:#ffffff;
    --peach:#fde9cb;
    --peach-deep:#f8dcb4;
    --ink:#1b1b1b;
    --muted:#b7a78b;
    --red:#e0262b;
    --sky:#a3ddfb;
    --sky-muted:#6cb6de;
    --lime:#e2fc90;
    --lime-icon:#9db252;
    --lime-muted:#b2c56a;
    --ice:#dfeef3;
    --ice-icon:#7fb0bb;
    --ice-muted:#9fb7bf;
    --mint:#c9e4dc;
    --mint-icon:#8ccbb3;
    --mint-muted:#9cc3b7;
    --lilac:#dccdf0;
    --lilac-icon:#b59ade;
    --lilac-muted:#b9a3da;
    --pink:#f0c9dc;
    --pink-icon:#d9a2c2;
    --pink-muted:#c898b4;
    --pill:#f3d9b6;
    --pill-text:#b69d7b;
  }
  *{box-sizing:border-box;margin:0;padding:0}
  html,body{width:1200px;height:1007px;overflow:hidden}
  body{background:var(--canvas);font-family:'Inter',sans-serif;color:var(--ink);position:relative}

  .screen-wrap{position:absolute;overflow:hidden;border-radius:30px;background:var(--screen)}
  .screen-wrap--primary{left:135px;top:134px;width:340px;height:738px}
  .screen-wrap--full{left:694px;top:54px;width:280px;height:910px}
  .screen{position:absolute;left:0;top:0;width:490px;height:1593px;transform-origin:0 0;background:var(--screen)}
  .screen-wrap--primary .screen{transform:scale(0.695)}
  .screen-wrap--full .screen{transform:scale(0.5714)}
  .screen > *{position:absolute}

  .profile{left:0;top:0;width:490px;height:300px;border-radius:52px;background:var(--peach);overflow:hidden}
  .avatar{position:absolute;left:30px;top:68px;width:104px;height:104px;border-radius:24px;background:linear-gradient(160deg,#fbe3a0,#f3c48c 55%,#bfe3ef);border:3px solid #fff}
  .badge-pro{position:absolute;left:53px;top:157px;width:58px;height:26px;border-radius:13px;background:#fff;font-size:14px;font-weight:700;display:flex;align-items:center;justify-content:center}
  .name{position:absolute;left:150px;top:94px;font-size:19px;font-weight:600}
  .handle{position:absolute;left:150px;top:124px;font-size:16px;color:var(--muted)}
  .more{position:absolute;left:405px;top:90px;width:52px;height:52px;border-radius:50%;background:#fdf0dc;display:flex;align-items:center;justify-content:center;gap:4px}
  .more i{width:4px;height:4px;border-radius:50%;background:var(--ink)}
  .stats{position:absolute;left:0;top:203px;width:490px;height:97px;background:var(--peach-deep);display:flex;align-items:center}
  .stat{flex:1;text-align:center;border-right:1.5px solid #f0cfa4;height:66px;display:flex;flex-direction:column;justify-content:center}
  .stat:last-child{border-right:none}
  .stat b{font-size:20px;font-weight:600;display:block}
  .stat span{font-size:13px;font-weight:500}
  .trophies{display:flex;justify-content:center;gap:9px;margin-bottom:2px}

  .muscle-card{left:32px;top:360px;width:426px;height:445px;border-radius:40px;background:linear-gradient(180deg,#fde5c4,#fde9cf 70%,#f9dfbe);overflow:hidden}
  .watermark{position:absolute;left:0;width:426px;text-align:center;font-size:76px;font-weight:800;color:rgba(233,140,120,.28);line-height:1}
  .watermark--top{top:185px}
  .watermark--bottom{top:275px}
  .body-map{left:90px;top:318px;width:310px;height:420px;border-radius:45% 45% 30% 30%;background:radial-gradient(ellipse at 50% 35%,#c8b04a 0%,#e96a5e 25%,rgba(232,90,80,.7) 45%,rgba(253,229,196,0) 72%)}
  .callout{font-size:17px;color:var(--red);font-weight:500}
  .callout--chest{left:366px;top:329px}
  .callout--biceps{left:370px;top:408px}
  .callout-lines{left:0;top:300px;width:490px;height:160px}
  .view-toggle{left:42px;top:737px;width:406px;height:58px}
  .view-toggle button{position:absolute;top:0;height:58px;border:none;border-radius:29px;font-family:inherit;font-size:14px;background:var(--pill);color:var(--pill-text)}
  .view-toggle .is-active{background:var(--ink);color:#fff}

  .ask-ai{left:32px;top:837px;width:426px;height:104px;border-radius:30px;background:var(--sky)}
  .orb{position:absolute;left:16px;top:20px;width:62px;height:62px;border-radius:50%;background:radial-gradient(circle at 35% 35%,#fff 0,#b9d2ff 25%,#7a6cf0 55%,#e27ad8 75%,#7ed7ff 100%);border:2px solid #fff}
  .ask-ai h2{position:absolute;left:93px;top:25px;font-size:25px;font-weight:500}
  .ask-ai p{position:absolute;left:93px;top:57px;font-size:15px;color:var(--sky-muted)}
  .go{width:42px;height:42px;border-radius:50%;background:#fff;display:flex;align-items:center;justify-content:center}
  .ask-ai .go{position:absolute;left:361px;top:31px}

  .tile{border-radius:28px;padding:20px}
  .tile .icon{width:62px;height:62px;border-radius:16px;display:flex;align-items:center;justify-content:center}
  .tile h3{font-size:24px;font-weight:500;line-height:1.25;margin-top:10px}
  .tile p{font-size:15px;line-height:1.3}
  .tile .go{width:40px;height:40px;margin-top:14px}
  .tile--food{left:32px;top:963px;width:160px;height:235px;background:var(--lime)}
  .tile--food .icon{background:var(--lime-icon)} .tile--food p{color:var(--lime-muted)}
  .tile--strength{left:214px;top:963px;width:244px;height:235px;background:var(--ice)}
  .tile--strength .icon{background:var(--ice-icon)} .tile--strength p{color:var(--ice-muted)}
  .tile--strength h3{margin-top:16px}
  .tile--workout{left:32px;top:1220px;width:245px;height:218px;background:var(--mint)}
  .tile--workout .icon{background:var(--mint-icon)} .tile--workout p{color:var(--mint-muted)}
  .tile--workout h3{margin-top:16px}
  .tile--form{left:299px;top:1220px;width:159px;height:343px;background:var(--lilac)}
  .tile--form .icon{background:var(--lilac-icon)} .tile--form p{color:var(--lilac-muted)}
  .tile--stats{left:32px;top:1460px;width:245px;height:103px;background:var(--pink);display:flex;align-items:center;gap:10px}
  .tile--stats .icon{background:var(--pink-icon);flex:none}
  .tile--stats h3{margin-top:0;font-size:24px} .tile--stats p{color:var(--pink-muted)}
</style>
</head>
<body>

<svg width="0" height="0" style="position:absolute">
  <defs>
    <symbol id="trophy" viewBox="0 0 20 22"><path d="M5 2h10v6a5 5 0 0 1-10 0z M5 4H2v2a3 3 0 0 0 3 3 M15 4h3v2a3 3 0 0 1-3 3 M10 13v4 M6 20h8 M7 17h6v3H7z" fill="#d9a418" stroke="#9a6a0a" stroke-width="1.3"/></symbol>
    <symbol id="arrow" viewBox="0 0 24 24"><path d="M4 12h15M13 6l6 6-6 6" fill="none" stroke="currentColor" stroke-width="2.2" stroke-linecap="round" stroke-linejoin="round"/></symbol>
    <symbol id="i-food" viewBox="0 0 40 40"><g fill="none" stroke="#eef6c4" stroke-width="2"><circle cx="20" cy="20" r="9"/><circle cx="20" cy="20" r="5"/><path d="M6 8v10M4 8v6a2 2 0 0 0 4 0V8M6 18v14M34 8c-3 2-3 9 0 11v13"/></g></symbol>
    <symbol id="i-arm" viewBox="0 0 40 40"><path d="M8 30c2-8 6-12 10-14l2-8 6 2-2 6c6 0 10 4 9 9-1 6-8 8-14 7-5-1-8-1-11-2z M17 24c3-2 7-2 9 1" fill="none" stroke="#e4f1f4" stroke-width="2" stroke-linejoin="round"/></symbol>
    <symbol id="i-dumbbell" viewBox="0 0 40 40"><path d="M6 16v8M11 12v16M29 12v16M34 16v8M11 20h18" fill="none" stroke="#e4f5ee" stroke-width="2.4" stroke-linecap="round"/></symbol>
    <symbol id="i-doc" viewBox="0 0 40 40"><path d="M11 6h13l6 6v22H11z M24 6v6h6 M15 18h11M15 23h11M15 28h8" fill="none" stroke="#efe6fa" stroke-width="2" stroke-linejoin="round"/></symbol>
    <symbol id="i-chart" viewBox="0 0 40 40"><path d="M7 7v26h27 M10 27l7-8 5 5 10-12" fill="none" stroke="#f8e4ef" stroke-width="2" stroke-linejoin="round" stroke-linecap="round"/></symbol>
  </defs>
</svg>

<div class="screen-wrap screen-wrap--primary">
  <div class="screen">
    <section class="profile">
      <div class="avatar" role="img" aria-label="Profile avatar of the user"></div>
      <span class="badge-pro">PRO</span>
      <div class="name">Marcus Hale</div>
      <div class="handle">@marcus</div>
      <div class="more"><i></i><i></i><i></i></div>
      <div class="stats">
        <div class="stat"><b>22.3k</b><span>Followers</span></div>
        <div class="stat"><b>10.7k</b><span>Following</span></div>
        <div class="stat"><b>107</b><span>Workouts</span></div>
        <div class="stat"><div class="trophies"><svg width="14" height="15"><use href="#trophy"/></svg><svg width="14" height="15"><use href="#trophy"/></svg><svg width="14" height="15"><use href="#trophy"/></svg></div><span>Trophy Case</span></div>
      </div>
    </section>
    <section class="muscle-card">
      <div class="watermark watermark--top">WORKOUT</div>
      <div class="watermark watermark--bottom">OVERVIEW</div>
    </section>
    <div class="body-map" role="img" aria-label="Front view anatomy figure with worked muscle groups highlighted"></div>
    <svg class="callout-lines" viewBox="0 0 490 160"><g fill="none" stroke="var(--red)" stroke-width="1.5"><path d="M357 36v65l-52 17-35 10"/><path d="M357 117h-16l-30 25-10 12"/></g><circle cx="357" cy="36" r="3" fill="var(--red)"/><circle cx="361" cy="117" r="3" fill="var(--red)"/><circle cx="270" cy="128" r="3" fill="var(--red)"/></svg>
    <span class="callout callout--chest">Chest</span>
    <span class="callout callout--biceps">Biceps</span>
    <div class="view-toggle">
      <button style="left:0;width:126px">Side View</button>
      <button class="is-active" style="left:134px;width:134px">Front View</button>
      <button style="left:276px;width:130px">Back View</button>
    </div>
    <section class="ask-ai">
      <div class="orb"></div>
      <h2>Ask FitBrook AI</h2>
      <p>Lorem Ipsum Dolor Ait Amet</p>
      <div class="go" style="color:var(--sky-muted)"><svg width="22" height="22"><use href="#arrow"/></svg></div>
    </section>
    <article class="tile tile--food"><div class="icon"><svg width="40" height="40"><use href="#i-food"/></svg></div><h3>Log Food</h3><p>Lorem Ipsum<br>Dolor Ait Amet</p></article>
    <article class="tile tile--strength"><div class="icon"><svg width="40" height="40"><use href="#i-arm"/></svg></div></article>
  </div>
</div>

<div class="screen-wrap screen-wrap--full">
  <div class="screen">
    <section class="profile">
      <div class="avatar" role="img" aria-label="Profile avatar of the user"></div>
      <span class="badge-pro">PRO</span>
      <div class="name">Marcus Hale</div>
      <div class="handle">@marcus</div>
      <div class="more"><i></i><i></i><i></i></div>
      <div class="stats">
        <div class="stat"><b>22.3k</b><span>Followers</span></div>
        <div class="stat"><b>10.7k</b><span>Following</span></div>
        <div class="stat"><b>107</b><span>Workouts</span></div>
        <div class="stat"><div class="trophies"><svg width="14" height="15"><use href="#trophy"/></svg><svg width="14" height="15"><use href="#trophy"/></svg><svg width="14" height="15"><use href="#trophy"/></svg></div><span>Trophy Case</span></div>
      </div>
    </section>
    <section class="muscle-card">
      <div class="watermark watermark--top">WORKOUT</div>
      <div class="watermark watermark--bottom">OVERVIEW</div>
    </section>
    <div class="body-map" role="img" aria-label="Front view anatomy figure with worked muscle groups highlighted"></div>
    <svg class="callout-lines" viewBox="0 0 490 160"><g fill="none" stroke="var(--red)" stroke-width="1.5"><path d="M357 36v65l-52 17-35 10"/><path d="M357 117h-16l-30 25-10 12"/></g><circle cx="357" cy="36" r="3" fill="var(--red)"/><circle cx="361" cy="117" r="3" fill="var(--red)"/><circle cx="270" cy="128" r="3" fill="var(--red)"/></svg>
    <span class="callout callout--chest">Chest</span>
    <span class="callout callout--biceps">Biceps</span>
    <div class="view-toggle">
      <button style="left:0;width:126px">Side View</button>
      <button class="is-active" style="left:134px;width:134px">Front View</button>
      <button style="left:276px;width:130px">Back View</button>
    </div>
    <section class="ask-ai">
      <div class="orb"></div>
      <h2>Ask FitBrook AI</h2>
      <p>Lorem Ipsum Dolor Ait Amet</p>
      <div class="go" style="color:var(--sky-muted)"><svg width="22" height="22"><use href="#arrow"/></svg></div>
    </section>
    <article class="tile tile--food"><div class="icon"><svg width="40" height="40"><use href="#i-food"/></svg></div><h3>Log Food</h3><p>Lorem Ipsum<br>Dolor Ait Amet</p><div class="go" style="color:var(--lime-icon)"><svg width="22" height="22"><use href="#arrow"/></svg></div></article>
    <article class="tile tile--strength"><div class="icon"><svg width="40" height="40"><use href="#i-arm"/></svg></div><h3>Strength Review</h3><p>Lorem Ipsum<br>Dolor Ait Amet</p><div class="go" style="color:var(--ice-icon)"><svg width="22" height="22"><use href="#arrow"/></svg></div></article>
    <article class="tile tile--workout"><div class="icon"><svg width="40" height="40"><use href="#i-dumbbell"/></svg></div><h3>Start Workout</h3><p>Lorem Ipsum Dolor Sit</p><div class="go" style="color:var(--mint-icon)"><svg width="22" height="22"><use href="#arrow"/></svg></div></article>
    <article class="tile tile--form"><div class="icon"><svg width="40" height="40"><use href="#i-doc"/></svg></div><h3>AI Form Review Tool</h3><p>Lorem Ipsum<br>Dolor Ait Amet</p><div class="go" style="color:var(--lilac-icon)"><svg width="22" height="22"><use href="#arrow"/></svg></div></article>
    <article class="tile tile--stats"><div class="icon"><svg width="40" height="40"><use href="#i-chart"/></svg></div><div><h3>Statistics</h3><p>Lorem Ipsum</p></div></article>
  </div>
</div>

</body>
</html>
```